Web design for Money Service Business (uncoded)

We need a very basic website with 5-6 pages. Home page, Services, Transfer(How to use our service), About us, Contact us, FAQ
Our company name is Meridale Exchange. We are a company that deals with currency exchange and international money transfer. We do cash exchange and international money transfers to bank accounts all over the world. We offer highly competitive exchange rates so usually attract customers who transfer money over $10,000. Our niche is with larger sums of money, the design needs to be professional and communicate trust, security and stability.

```html
<!DOCTYPE html>
<html lang="en">
<head>
<meta charset="utf-8">
<title>Meridale Exchange – International Money Transfer</title>
<link rel="stylesheet" href="https://fonts.googleapis.com/css2?family=Jura:wght@400;500&family=Open+Sans:wght@400;600;700&display=swap">
<style>
  :root {
    --blue: #1d5a8e;
    --blue-dark: #1a4f7d;
    --orange: #f39a12;
    --text: #333;
    --muted: #666;
    --line: #d6d6d6;
    --panel: #ececec;
    --header-bg: #f3f3f3;
    --nav-bg: #f6f6f6;
    --hero-dark: #3a3a3a;
  }
  * { box-sizing: border-box; margin: 0; padding: 0; }
  html, body { width: 1120px; height: 1200px; overflow: hidden; }
  body { font-family: "Open Sans", Arial, sans-serif; color: var(--text); background: #fff; position: relative; }
  .heading-font { font-family: "Jura", "Open Sans", sans-serif; }

  .top-rule { height: 4px; background: var(--blue); position: relative; }
  .top-rule::after { content: ""; position: absolute; left: 162px; width: 798px; top: 0; bottom: 0; background: var(--orange); }

  .site-header { height: 102px; background: var(--header-bg); position: relative; }
  .brand { position: absolute; left: 164px; top: 26px; }
  .brand-name { display: flex; align-items: center; gap: 8px; font-family: "Jura", sans-serif; font-weight: 500; font-size: 33px; color: var(--blue); letter-spacing: 1px; line-height: 1; text-transform: uppercase; }
  .brand-name .mark { width: 22px; height: 22px; border-radius: 50%; border: 3px solid var(--blue); }
  .brand-tagline { font-family: "Jura", sans-serif; font-size: 13.5px; letter-spacing: 4.2px; color: var(--blue); margin-top: 6px; }
  .header-contact { position: absolute; right: 160px; top: 50px; display: flex; gap: 20px; font-size: 13px; color: #666; }
  .contact-item { display: flex; align-items: center; gap: 5px; }
  .contact-item svg { fill: #999; }

  .main-nav { height: 46px; background: var(--nav-bg); border-top: 1px solid #e2e2e2; position: relative; }
  .nav-list { position: absolute; left: 162px; top: 0; display: flex; list-style: none; border-left: 1px solid var(--line); }
  .nav-list li { height: 45px; padding: 0 19px; border-right: 1px solid var(--line); display: flex; align-items: center; font-size: 13px; color: #555; }
  .nav-list li.active { color: var(--orange); }
  .social { position: absolute; right: 160px; top: 8px; display: flex; align-items: center; gap: 4px; font-size: 13px; color: var(--orange); }
  .social span { margin-right: 6px; }
  .social .dot { width: 26px; height: 26px; border-radius: 50%; border: 2px solid #bbb; }

  .hero { height: 302px; background: var(--hero-dark); position: relative; }
  .hero-photo { position: absolute; left: 162px; width: 798px; top: 0; bottom: 0;
    background: linear-gradient(120deg, #c7ccd0 0%, #8e969c 25%, #c9b98c 45%, #4f5a63 65%, #2b3540 100%); }
  .hero-caption { position: absolute; left: 162px; width: 798px; top: 0; height: 101px; background: rgba(30,30,30,.82); text-align: right; padding: 26px 20px 0 0; }
  .hero-caption h1 { font-family: "Jura", sans-serif; font-weight: 500; font-size: 26px; color: #2a7bc0; letter-spacing: -.3px; }
  .hero-caption p { font-size: 13px; color: #eee; margin-top: 6px; }

  .content { position: absolute; top: 456px; left: 165px; width: 795px; }
  .main-col { position: absolute; left: 0; top: 36px; width: 543px; }
  .welcome { font-family: "Jura", sans-serif; font-weight: 500; font-size: 25px; color: #333; letter-spacing: -.5px; }
  .welcome .accent-blue { color: var(--blue); }
  .welcome .accent-orange { color: var(--orange); }
  .section-title { font-family: "Jura", sans-serif; font-weight: 500; font-size: 19px; color: var(--orange); margin-top: 10px; }
  .lead { font-size: 14.5px; line-height: 21px; color: var(--blue); text-align: justify; margin-top: 4px; }

  .two-col { display: flex; justify-content: space-between; margin-top: 20px; }
  .two-col > div { width: 250px; }
  .two-col h3 { font-size: 13px; font-weight: 600; color: #555; margin-bottom: 6px; }
  .two-col p { font-size: 11.5px; line-height: 19px; color: #555; text-align: justify; padding-left: 2px; }
  .two-col p + p { margin-top: 19px; }
  .check-list { list-style: none; margin-top: 6px; }
  .check-list li { font-size: 11.5px; color: #333; height: 29px; display: flex; align-items: center; gap: 6px; border-bottom: 1px dotted #ccc; padding-left: 1px; }

  .why-box { margin-top: 28px; margin-left: 2px; border: 1px solid #d0d0d0; border-radius: 3px; height: 133px; background: linear-gradient(#f4f4f4, #fff 30px); padding: 14px 10px 0; }
  .why-box h2 { font-family: "Jura", sans-serif; font-weight: 500; font-size: 19px; color: var(--blue); text-align: center; }
  .why-grid { display: grid; grid-template-columns: 265px 1fr; margin-top: 6px; }
  .why-grid li { list-style: none; font-size: 11.5px; height: 25.6px; display: flex; align-items: center; gap: 9px; color: #333; }
  .why-grid li::before { content: ""; border-left: 5px solid var(--orange); border-top: 4px solid transparent; border-bottom: 4px solid transparent; }

  .side-col { position: absolute; left: 571px; top: 42px; width: 224px; }
  .promo { height: 122px; background: var(--orange); position: relative; overflow: hidden; color: #fff; }
  .promo .upto { position: absolute; left: 39px; top: 6px; font-family: Georgia, serif; font-style: italic; font-size: 17px; }
  .promo .pct { position: absolute; left: 16px; top: 22px; font-family: Georgia, serif; font-style: italic; font-size: 48px; line-height: 1; }
  .promo .pct small { font-size: 24px; }
  .promo .label { position: absolute; left: 15px; top: 80px; font-weight: 700; font-size: 14.5px; line-height: 15px; }
  .promo .globe { position: absolute; left: 126px; top: 26px; width: 76px; height: 76px; border-radius: 50%; background: #fff; }
  .promo .corner { position: absolute; right: 0; bottom: 0; width: 0; height: 0; border-left: 62px solid transparent; border-bottom: 62px solid var(--blue-dark); }
  .promo .corner-text { position: absolute; right: 3px; bottom: 12px; font-size: 8px; font-weight: 600; line-height: 9px; transform: rotate(-45deg); text-align: center; }

  .news { margin-top: 18px; background: var(--panel); height: 390px; padding: 12px 9px 0 12px; }
  .news h2 { font-family: "Jura", sans-serif; font-weight: 500; font-size: 21px; color: var(--orange); }
  .news-item { padding-left: 2px; }
  .news-item + .news-item { border-top: 1px dotted #aaa; margin-top: 14px; padding-top: 12px; margin-right: 6px; }
  .news-item h3 { font-weight: 400; font-size: 13px; line-height: 14px; color: #555; margin-top: 12px; }
  .news-item + .news-item h3 { margin-top: 0; }
  .news-item time { display: block; font-size: 11.5px; color: #777; margin-top: 6px; }
  .news-item p { font-size: 11.5px; line-height: 19px; color: #333; margin-top: 2px; }
  .read-more { font-size: 11.5px; color: var(--blue); margin-top: 2px; display: inline-block; }

  .site-footer { position: absolute; left: 0; top: 1080px; width: 1120px; height: 120px; background: var(--blue-dark); border-top: 6px solid #2366a0; }
  .footer-nav { position: absolute; left: 166px; top: 40px; display: flex; font-size: 13.5px; color: #fff; list-style: none; }
  .footer-nav li + li::before { content: "|"; margin: 0 9px; }
  .copyright { position: absolute; left: 166px; top: 74px; font-size: 11.5px; color: #4f8ac0; }
  .footer-contact { position: absolute; left: 677px; top: 42px; }
  .footer-contact h4 { font-weight: 400; font-size: 13.5px; color: var(--orange); }
  .footer-contact .row { display: flex; gap: 20px; margin-top: 6px; font-size: 13.5px; color: #fff; }
  .footer-contact svg { fill: #ccd; }
</style>
</head>
<body>
  <div class="top-rule"></div>

  <header class="site-header">
    <div class="brand">
      <div class="brand-name"><span class="mark"></span>Meridale Exchange</div>
      <div class="brand-tagline">INTERNATIONAL MONEY TRANSFER</div>
    </div>
    <div class="header-contact">
      <span class="contact-item"><svg width="12" height="10" viewBox="0 0 12 10"><path d="M0 0h12v10H0z M1 1l5 4 5-4" stroke="#fff" stroke-width="1"/></svg>info@meridaleexchange.com</span>
      <span class="contact-item"><svg width="8" height="13" viewBox="0 0 8 13"><rect x="0" y="0" width="8" height="13" rx="1.5"/><rect x="1.5" y="1.5" width="5" height="8" fill="#fff"/></svg>+12 40215 78930</span>
    </div>
  </header>

  <nav class="main-nav">
    <ul class="nav-list">
      <li class="active">HOME</li><li>SERVICES</li><li>TRANSFER</li><li>ABOUT US</li><li>CONTACT US</li><li>FAQ</li>
    </ul>
    <div class="social"><span>Follow us on</span><i class="dot"></i><i class="dot"></i><i class="dot"></i></div>
  </nav>

  <section class="hero">
    <div class="hero-photo" role="img" aria-label="Upward view of a curved glass and steel office building"></div>
    <div class="hero-caption">
      <h1>INTERNATIONAL MONEY TRANSFER</h1>
      <p>We do cash exchange and international money transfers to bank accounts all over the world</p>
    </div>
  </section>

  <main class="content">
    <div class="main-col">
      <h1 class="welcome">WELCOME TO <span class="accent-blue">MERIDALE</span> <span class="accent-orange">EXCHANGE</span></h1>
      <h2 class="section-title">ABOUT THE COMPANY</h2>
      <p class="lead">Curabitur vel diam in massa porttitor dictum id in lorem. Vivamus faucibus ac leo ac dignissim. Maecenas orci est, euismod facilisis feugiat sit amet, semper ut tortor. Donec eleifend accumsan nisl, nec laoreet leo iaculis sit amet. Vivamus varius arcu eu sagittis aliquam. Vivamus accumsan cursus hendrerit.</p>

      <div class="two-col">
        <div>
          <h3>Who we are</h3>
          <p>Nam vulputate mauris id arcu pharetra, sed posuere quam cursus. Nullam eget massa vel mi posuere venenatis sed quis tortor. In hac habitasse platea dictumst.</p>
          <p>Fusce nisi tellus, fermentum a luctus eget, convallis vitae orci. In commodo egestas magna quis placerat. Quisque adipiscing consequat nisi, nec accumsan quam venenatis ac.</p>
        </div>
        <div>
          <h3>What we do</h3>
          <p>Nam vulputate mauris id arcu pharetra, sed posuere quam cursus.</p>
          <ul class="check-list">
            <li><svg width="10" height="10" viewBox="0 0 10 10"><circle cx="5" cy="5" r="5" fill="#f39a12"/><path d="M2.6 5.2l1.7 1.6 3.2-3.3" stroke="#fff" stroke-width="1.4" fill="none"/></svg>Nullam eget massa vel mi posuere</li>
            <li><svg width="10" height="10" viewBox="0 0 10 10"><circle cx="5" cy="5" r="5" fill="#f39a12"/><path d="M2.6 5.2l1.7 1.6 3.2-3.3" stroke="#fff" stroke-width="1.4" fill="none"/></svg>Venenatis sed quis tortor</li>
            <li><svg width="10" height="10" viewBox="0 0 10 10"><circle cx="5" cy="5" r="5" fill="#f39a12"/><path d="M2.6 5.2l1.7 1.6 3.2-3.3" stroke="#fff" stroke-width="1.4" fill="none"/></svg>In hac habitasse platea dictumst.</li>
            <li><svg width="10" height="10" viewBox="0 0 10 10"><circle cx="5" cy="5" r="5" fill="#f39a12"/><path d="M2.6 5.2l1.7 1.6 3.2-3.3" stroke="#fff" stroke-width="1.4" fill="none"/></svg>Fusce nisi tellus fermentum a luctus</li>
            <li><svg width="10" height="10" viewBox="0 0 10 10"><circle cx="5" cy="5" r="5" fill="#f39a12"/><path d="M2.6 5.2l1.7 1.6 3.2-3.3" stroke="#fff" stroke-width="1.4" fill="none"/></svg>In commodo egestas magna quis</li>
          </ul>
        </div>
      </div>

      <section class="why-box">
        <h2>WHY SHOULD YOU CHOOSE US</h2>
        <ul class="why-grid">
          <li>Cras accumsan orci mauris ut aliquam</li><li>Cras accumsan orci mauris ut aliquam</li>
          <li>Ipsum Fusce quam dui accumsan a magna</li><li>Ipsum Fusce quam dui accumsan a magna</li>
          <li>Faucibus Vestibulum sapien leo</li><li>Faucibus Vestibulum sapien leo</li>
        </ul>
      </section>
    </div>

    <aside class="side-col">
      <div class="promo">
        <span class="upto">upto</span>
        <span class="pct">20<small>% off</small></span>
        <span class="label">ON MONEY<br>TRANSFER ›</span>
        <div class="globe" role="img" aria-label="White globe showing the Americas"></div>
        <div class="corner"></div>
        <span class="corner-text">KNOW<br>MORE</span>
      </div>

      <section class="news">
        <h2>NEWS &amp; EVENTS</h2>
        <article class="news-item">
          <h3>Vestibulum lacinia congue commodo</h3>
          <time>November 10, 2013</time>
          <p>Sed ullamcorper enim quis dolor pellentesque dictum. Integer convallis, massa tincidunt laoreet auctor, mi ante pretium lacus, ac congue odio ante non nunc....</p>
          <span class="read-more">Read More ›</span>
        </article>
        <article class="news-item">
          <h3>Praesent cursus lacus ac eros</h3>
          <time>November 9, 2013</time>
          <p>Sed ullamcorper enim quis dolor pellentesque dictum. Integer convallis, massa tincidunt laoreet auctor, mi ante pretium lacus, ac congue odio ante non nunc....</p>
          <span class="read-more">Read More ›</span>
        </article>
      </section>
    </aside>
  </main>

  <footer class="site-footer">
    <ul class="footer-nav"><li>Home</li><li>Services</li><li>Transfer</li><li>About us</li><li>Contact us</li><li>FAQ</li></ul>
    <p class="copyright">Copyright © 2013 Meridale Exchange. All rights reserved</p>
    <div class="footer-contact">
      <h4>Contact us</h4>
      <div class="row">
        <span class="contact-item"><svg width="12" height="10" viewBox="0 0 12 10"><path d="M0 0h12v10H0z"/><path d="M1 1l5 4 5-4" stroke="#1a4f7d" fill="none"/></svg>info@meridaleexchange.com</span>
        <span class="contact-item"><svg width="8" height="13" viewBox="0 0 8 13"><rect width="8" height="13" rx="1.5"/><rect x="1.5" y="1.5" width="5" height="8" fill="#1a4f7d"/></svg>+12 40215 78930</span>
      </div>
    </div>
  </footer>
</body>
</html>
```